Pilates Classes Flyer Design

I need a flyer designed that will promote my range of classes held in Bath, UK. I teach beginners, intermediate level and Over 50's and 60's and also teach individuals in their own homes. I would like to see designs using my colours blue Pantone 306 and Lime Green 14-0452 TPX TCX. The flyer should reflect a friendly, welcoming and professional class structure. I attach an old flyer for your reference and copy.

Target Market(s)

Men and Women who have busy lives working hard, who recognise they need to stretch out, do some exercise and de-stress after a busy day

Ladies over 50 who want to do some Pilates in a friendly fun environment and meet people at the same time.

Industry/Entity Type

It Professional

Font styles to use
Sans Serif
Script

Requirements
Must have
• One-sided flyer
Text only logo. Drop the figure

```html
<!DOCTYPE html>
<html lang="en">
<head>
<meta charset="utf-8">
<title>CoreFlow Pilates – Class Flyer</title>
<link rel="stylesheet" href="https://fonts.googleapis.com/css2?family=Lato:wght@300;400;700&display=swap">
<style>
  :root {
    --blue: #1fa9e1;
    --blue-deep: #0b6e9a;
    --navy: #1d5f7e;
    --lime: #8dc63f;
    --lime-soft: #c9e59a;
    --teal: #1b8a9c;
    --paper: #f7f8f8;
    --sky-top: #b9e3f4;
    --sky-bottom: #e6f5fb;
    --backdrop: #e9ecee;
  }
  * { box-sizing: border-box; margin: 0; padding: 0; }
  html, body { width: 990px; height: 1200px; overflow: hidden; }
  body {
    background: var(--backdrop);
    font-family: "Lato", Arial, sans-serif;
    position: relative;
  }
  .flyer {
    position: absolute; left: 108px; top: 48px;
    width: 770px; height: 1085px;
    background: var(--paper);
    overflow: hidden;
    box-shadow: 0 6px 24px rgba(0,0,0,.18);
  }
  .hero-photo {
    position: absolute; left: 0; top: 0; width: 770px; height: 270px;
    background: linear-gradient(100deg, #c9a58a 0%, #e8d6c6 25%, #b9c7d3 55%, #9fb6c9 80%, #d7e1ea 100%);
  }
  .hero-curve { position: absolute; left: 0; top: 190px; width: 770px; height: 110px; }
  .cert-badge {
    position: absolute; left: 268px; top: 170px; width: 212px; height: 70px;
    background: var(--teal); border: 4px solid var(--lime-soft); border-radius: 8px;
  }
  .brand {
    position: absolute; top: 270px; width: 100%; text-align: center;
    font-weight: 300; color: var(--blue); font-size: 62px; letter-spacing: 1px;
  }
  .headline {
    position: absolute; top: 388px; width: 100%; text-align: center;
    font-size: 33px; color: var(--lime); font-weight: 400;
  }
  .headline strong { color: var(--blue); font-weight: 700; }
  .intro {
    position: absolute; top: 438px; width: 100%; text-align: center;
    font-size: 16px; line-height: 1.4; color: var(--blue); font-weight: 400;
  }
  .intro em { font-style: normal; color: var(--lime); }
  .benefit { position: absolute; left: 118px; }
  .benefit svg { position: absolute; left: 0; top: 6px; width: 48px; height: 42px; }
  .benefit h3 { margin-left: 70px; font-size: 18px; font-weight: 400; color: var(--blue); }
  .benefit p { margin-left: 70px; font-size: 15px; font-weight: 300; color: var(--blue); margin-top: 4px; }
  .benefit-one { top: 517px; }
  .benefit-two { top: 603px; }
  .classes-tab {
    position: absolute; left: 116px; top: 716px; width: 560px; height: 52px;
    background: var(--lime); border-radius: 12px 12px 0 0;
    color: #fff; font-weight: 700; font-size: 22px; text-align: center; line-height: 52px;
  }
  .venues {
    position: absolute; left: 0; top: 767px; width: 770px; height: 208px;
    background: linear-gradient(var(--sky-top), var(--sky-bottom));
    text-align: center; padding-top: 28px;
  }
  .venue h4 { font-size: 17px; font-weight: 700; color: var(--navy); }
  .venue p { font-size: 13px; color: var(--navy); margin: 3px 0 13px; }
  .contact-bar {
    position: absolute; left: 0; top: 975px; width: 770px; height: 110px;
    background: linear-gradient(var(--blue), var(--blue-deep));
    border-top: 5px solid var(--lime); color: #fff;
  }
  .phone-icon { position: absolute; left: 36px; top: 28px; width: 76px; height: 56px; }
  .call { position: absolute; left: 124px; top: 20px; }
  .call span { display: block; font-size: 24px; font-weight: 300; letter-spacing: 1px; }
  .call strong { display: block; font-size: 31px; font-weight: 700; line-height: 1; }
  .divider { position: absolute; left: 358px; top: 26px; width: 3px; height: 58px; background: #fff; }
  .email { position: absolute; left: 380px; top: 40px; font-size: 23px; }
</style>
</head>
<body>
<main class="flyer">
  <div class="hero-photo" role="img" aria-label="Photo of smiling people on exercise bikes in a bright gym class"></div>
  <svg class="hero-curve" viewBox="0 0 770 110" preserveAspectRatio="none" aria-hidden="true">
    <path d="M0 60 Q385 0 770 55 L770 110 L0 110 Z" fill="var(--lime)"/>
    <path d="M0 72 Q385 16 770 66 L770 110 L0 110 Z" fill="var(--lime-soft)"/>
    <path d="M0 82 Q385 26 770 76 L770 110 L0 110 Z" fill="var(--paper)"/>
  </svg>
  <div class="cert-badge" aria-hidden="true"></div>

  <h1 class="brand">CoreFlow Pilates</h1>
  <h2 class="headline">— NEW <strong>CLASSES</strong> NEAR YOU! —</h2>
  <p class="intro">Pilates is for <em>EVERYONE</em> whatever level of fitness, age or ability<br>to help you build strength, flexibility and overall well-being.</p>

  <div class="benefit benefit-one">
    <svg viewBox="0 0 48 42" aria-hidden="true"><path d="M2 24 L10 18 L18 28 L42 2 L47 8 L18 40 Z" fill="var(--lime)"/></svg>
    <h3>Quality teaching with Balance Method Teacher.</h3>
    <p>Progressive approach. Teaching good movement skills.</p>
  </div>
  <div class="benefit benefit-two">
    <svg viewBox="0 0 48 42" aria-hidden="true"><path d="M2 24 L10 18 L18 28 L42 2 L47 8 L18 40 Z" fill="var(--lime)"/></svg>
    <h3>Small class sizes and friendly atmosphere.</h3>
    <p>Beginners, Intermediate and Over 50’s classes to choose from.</p>
  </div>

  <div class="classes-tab">JOIN MY ONE-HOUR CLASSES AT</div>
  <section class="venues">
    <div class="venue"><h4>ST AIDAN’S CHURCH HALL, OAK FLAT</h4><p>Monday evenings, Tuesday and Friday mornings.</p></div>
    <div class="venue"><h4>MILLBROOK MEADOWS DR. SURGERY</h4><p>Tuesday evenings.</p></div>
    <div class="venue"><h4>HARWOOD CENTRE, LINDEN ROAD,</h4><p>Wednesday mornings and evenings.</p></div>
  </section>

  <footer class="contact-bar">
    <svg class="phone-icon" viewBox="0 0 76 56" aria-hidden="true">
      <path d="M4 20 Q4 4 38 4 Q72 4 72 20 L72 26 L56 26 L56 18 L20 18 L20 26 L4 26 Z" fill="#fff"/>
      <path d="M14 30 L24 22 L52 22 L62 30 L66 52 L10 52 Z" fill="#fff"/>
      <circle cx="38" cy="37" r="8" fill="var(--blue)"/>
    </svg>
    <div class="call"><span>CALL TESSA ON</span><strong>07700900123</strong></div>
    <div class="divider"></div>
    <div class="email">tessa.marlow@example.co.uk</div>
  </footer>
</main>
</body>
</html>
```